Tavo Payments Business card refresh

Need a new design of our business card The info is not what is on these cards i sent this for a reference. I can email all the info over
Info would be Derek Whitfield Chief TAVO is the title. our new address is 47615 Birch Hollow Rd. Westlake Village Ca 91384 Cell number is 805-634-2917 Work number is 855-482-7309 ext 212 Derek@tavopayments.com is my email address
Target Market(s)
Merchant Services all businesses that take credit cards
Industry/Entity Type
Merchant Services / Credit Card processing
Contact Information for Business Card
Need a new design of our business card The info is not what is on these cards i sent this for a reference. I can email all the info over Info would be Derek Whitfield Chief TAVO is the title. our new address is 47615 Birch Hollow Rd. Westlake Village Ca 91384 Cell number is 805-634-2917 Work number is 855-482-7309 ext 212 Derek@tavopayments.com is my email address
Requirements
Must have
- My logo and colors from my brand guidelines
Nice to have
- i sent some designs just need a new refresh
Should not have
- nothing specific

```html
<!DOCTYPE html>
<html lang="en">
<head>
<meta charset="utf-8">
<title>Tavo Payments – Business Card</title>
<link rel="stylesheet" href="https://fonts.googleapis.com/css2?family=Poppins:wght@400;500;600;700&display=swap">
<style>
  :root {
    --page: #ececec;
    --card: #2a2e33;
    --green: #97c100;
    --white: #ffffff;
    --ink: #2a2e33;
    --shadow: rgba(0,0,0,0.28);
  }
  * { box-sizing: border-box; margin: 0; padding: 0; }
  html, body {
    width: 1200px; height: 1200px; overflow: hidden;
    background: var(--page);
    font-family: "Poppins", sans-serif;
  }
  .canvas { position: relative; width: 1200px; height: 1200px; }

  .card {
    position: absolute; left: 181px; width: 838px; height: 478px;
    background: var(--card);
    box-shadow: 24px 24px 18px var(--shadow);
    overflow: hidden;
  }
  .card--front { top: 110px; }
  .card--back { top: 611px; }

  .band {
    position: absolute; left: 0; bottom: 0; width: 100%; height: 53px;
    background: var(--green); color: var(--ink);
    display: flex; align-items: center; justify-content: center;
    white-space: nowrap;
  }

  /* Front */
  .brand {
    position: absolute; left: 0; width: 418px; top: 150px;
    text-align: center; color: var(--white); font-weight: 600;
  }
  .brand__name { display: block; font-size: 92px; line-height: 1; letter-spacing: 2px; }
  .brand__sub { display: block; font-size: 22px; letter-spacing: 17px; margin-top: 14px; padding-left: 17px; }

  .divider {
    position: absolute; left: 418px; top: 48px; width: 2px; height: 328px;
    background: var(--green);
  }

  .icon { position: absolute; left: 462px; width: 28px; height: 28px; fill: var(--green); }
  .icon--person { top: 66px; }
  .icon--phone { top: 162px; }
  .icon--web { top: 259px; }

  .person { position: absolute; left: 513px; top: 60px; }
  .person__name { color: var(--white); font-size: 38px; font-weight: 500; line-height: 1.1; white-space: nowrap; }
  .person__title { color: var(--green); font-size: 19px; line-height: 1.3; }

  .contacts { position: absolute; left: 513px; top: 155px; list-style: none; }
  .contacts li { color: var(--white); font-size: 19px; line-height: 29.5px; font-weight: 500; white-space: nowrap; }
  .contacts .label { color: var(--green); font-weight: 400; }

  .email { position: absolute; left: 513px; top: 258px; color: var(--white); font-size: 19px; font-weight: 500; white-space: nowrap; }

  .accepted { position: absolute; left: 467px; top: 315px; display: flex; gap: 9px; }
  .accepted__item {
    width: 68px; height: 43px; border-radius: 3px;
    background: var(--white); color: var(--ink);
    display: flex; align-items: center; justify-content: center;
    font-size: 12px; font-weight: 600;
  }

  .address { font-size: 23px; font-weight: 500; letter-spacing: 1px; }

  /* Back */
  .brand--small { left: auto; right: 26px; top: 30px; width: auto; text-align: center; }
  .brand--small .brand__name { font-size: 32px; letter-spacing: 1px; }
  .brand--small .brand__sub { font-size: 8px; letter-spacing: 5px; margin-top: 2px; padding-left: 5px; }

  .services { position: absolute; top: 115px; list-style: none; }
  .services--left { left: 74px; }
  .services--right { left: 460px; }
  .services li {
    color: var(--white); font-size: 27px; line-height: 45px;
    position: relative; padding-left: 17px; white-space: nowrap;
  }
  .services li::before {
    content: ""; position: absolute; left: 0; top: 20px;
    width: 6px; height: 6px; border-radius: 50%; background: var(--green);
  }

  .tagline {
    position: absolute; left: 0; width: 100%; top: 363px; text-align: center;
    color: var(--green); font-size: 35px; font-weight: 700; letter-spacing: 0.3px; white-space: nowrap;
  }
  .referral { font-size: 27px; font-weight: 500; }
</style>
</head>
<body>
<main class="canvas">

  <section class="card card--front" aria-label="Business card front">
    <div class="brand">
      <span class="brand__name">TAVO</span>
      <span class="brand__sub">PAYMENTS</span>
    </div>

    <div class="divider"></div>

    <svg class="icon icon--person" viewBox="0 0 28 28" aria-hidden="true">
      <circle cx="14" cy="7" r="6"/>
      <path d="M1 28v-4c0-5 4-9 9-9h8c5 0 9 4 9 9v4z"/>
    </svg>
    <div class="person">
      <p class="person__name">Derek Whitfield</p>
      <p class="person__title">Chief TAVO</p>
    </div>

    <svg class="icon icon--phone" viewBox="0 0 28 28" aria-hidden="true">
      <path d="M7 2l4 6-3 3c1 3 4 6 7 7l3-3 6 4-2 5c-1 1-3 1-5 0C10 21 5 16 2 9 1 7 1 5 2 4z"/>
      <path d="M16 4a9 9 0 0 1 8 8h-2a7 7 0 0 0-6-6z M16 8a5 5 0 0 1 4 4h-2a3 3 0 0 0-2-2z"/>
    </svg>
    <ul class="contacts">
      <li><span class="label">C:</span> 805-634-2917</li>
      <li><span class="label">O:</span> 855-482-7309 ext 212</li>
      <li><span class="label">F:</span> 888-417-6250</li>
    </ul>

    <svg class="icon icon--web" viewBox="0 0 28 28" aria-hidden="true">
      <path d="M14 1a13 13 0 1 0 0 26 13 13 0 0 0 0-26zm0 2.5c1.6 1.6 2.8 4.6 3.1 8.2H10.9c.3-3.6 1.5-6.6 3.1-8.2zM3.6 12.3c.4-3.5 2.7-6.4 5.8-7.7-1 2-1.7 4.7-1.9 7.7zm0 3.4h3.9c.2 3 .9 5.7 1.9 7.7-3.1-1.3-5.4-4.2-5.8-7.7zM14 24.5c-1.6-1.6-2.8-4.6-3.1-8.8h6.2c-.3 4.2-1.5 7.2-3.1 8.8zm4.6-1.1c1-2 1.7-4.7 1.9-7.7h3.9c-.4 3.5-2.7 6.4-5.8 7.7zm1.9-11.1c-.2-3-.9-5.7-1.9-7.7 3.1 1.3 5.4 4.2 5.8 7.7z"/>
    </svg>
    <p class="email">Derek@tavopayments.com</p>

    <div class="accepted" aria-label="Accepted cards">
      <span class="accepted__item">Vexa</span>
      <span class="accepted__item">Meridian</span>
      <span class="accepted__item">Novacard</span>
      <span class="accepted__item">Strata</span>
    </div>

    <div class="band">
      <p class="address">47615 Birch Hollow Rd. Westlake Village, Ca, 91384</p>
    </div>
  </section>

  <section class="card card--back" aria-label="Business card back">
    <div class="brand brand--small">
      <span class="brand__name">TAVO</span>
      <span class="brand__sub">PAYMENTS</span>
    </div>

    <ul class="services services--left">
      <li>Credit Card Processing</li>
      <li>Check Guarantee</li>
      <li>Gift Cards</li>
      <li>Loyalty Cards</li>
      <li>ACH Deposits</li>
    </ul>
    <ul class="services services--right">
      <li>24/7 Customer Support</li>
      <li>Same Day Approvals</li>
      <li>ATM Sales</li>
      <li>ATM Placement</li>
      <li>Merchant Funding</li>
    </ul>

    <p class="tagline">BEST RATES, BEST SERVICE - GUARANTEED</p>

    <div class="band">
      <p class="referral">Ask about our “ Merchant Referral ” Program</p>
    </div>
  </section>

</main>
</body>
</html>
```